Hydrographic business needs a business card that reaches hunters and off-road enthusiasts

We need a business card for a new hydrographics company catering to customers such as hunters, off-road ATV riders and custom vehicle enthusiasts. A western theme is preferred but professional. Our service should be thought of as upper end graphic design on firearms, off road vehicles, motorcycles, etc... See www.caldorfx.com for ideas on patterns, colors, etc...

Target Market(s)

Hunters, off road enthusiasts, custom car enthusiasts, motorcycle riders...

Industry/Entity Type

Graphic Design

```html
<!DOCTYPE html>
<html lang="en">
<head>
<meta charset="utf-8">
<title>Caldor Hydro Graphics – Business Card</title>
<link href="https://fonts.googleapis.com/css2?family=Open+Sans:wght@400;600;700;800&display=swap" rel="stylesheet">
<style>
  :root {
    --canvas: #cfd0d0;
    --forest: #3d7623;
    --forest-deep: #336a1d;
    --sage: #9db556;
    --khaki: #c9cf8a;
    --olive: #7f9f45;
    --paper: #f5f5f3;
    --ink-light: #ffffff;
  }
  * { margin: 0; padding: 0; box-sizing: border-box; }
  html, body {
    width: 1200px; height: 1000px; overflow: hidden;
    background: var(--canvas);
    font-family: "Open Sans", Arial, sans-serif;
  }
  .card {
    position: absolute;
    left: 250px;
    width: 700px; height: 400px;
    overflow: hidden;
    box-shadow: 0 6px 18px rgba(0,0,0,0.18);
  }
  .card--front { top: 60px; background: var(--forest); }
  .card--back  { top: 540px; background: var(--forest); color: var(--ink-light); }

  .card-art { position: absolute; inset: 0; }

  .brand {
    position: absolute;
    top: 118px; left: 0; right: 0;
    display: flex; align-items: center; justify-content: center; gap: 14px;
    color: var(--forest);
    font-weight: 800;
    font-size: 40px;
    letter-spacing: 0.5px;
  }
  .brand__dot {
    width: 30px; height: 30px; border-radius: 50%;
    background: var(--sage);
  }

  .person { position: absolute; left: 388px; top: 50px; }
  .person__name { font-size: 26px; font-weight: 700; letter-spacing: 0.5px; line-height: 1.2; }
  .person__role { font-size: 14px; font-weight: 600; }

  .contact {
    position: absolute; left: 350px; top: 152px;
    list-style: none;
    font-size: 19px; font-weight: 600; line-height: 30px;
  }
  .contact__item--address { margin-bottom: 16px; }
  .contact__label { display: inline-block; width: 32px; }
  .contact__indent { padding-left: 32px; }
</style>
</head>
<body>
  <section class="card card--front" aria-label="Card front">
    <svg class="card-art" viewBox="0 0 700 400" width="700" height="400" aria-hidden="true">
      <path d="M0 0 H700 V190 C560 330 380 350 250 335 C140 322 50 250 0 130 Z" fill="var(--paper)"/>
      <path d="M0 100 C50 225 140 295 250 308 C380 323 560 305 700 160" fill="none" stroke="var(--sage)" stroke-width="16"/>
    </svg>
    <div class="brand">
      <span class="brand__dot"></span>
      <span class="brand__name">Caldor Hydro Graphics</span>
    </div>
  </section>

  <section class="card card--back" aria-label="Card back">
    <svg class="card-art" viewBox="0 0 700 400" width="700" height="400">
      <defs>
        <radialGradient id="camoTone" cx="0.4" cy="0.5" r="0.7">
          <stop offset="0" stop-color="var(--olive)"/>
          <stop offset="0.6" stop-color="var(--sage)"/>
          <stop offset="1" stop-color="var(--khaki)"/>
        </radialGradient>
      </defs>
      <circle cx="40" cy="330" r="270" fill="url(#camoTone)" role="img" aria-label="Camouflage pattern area"/>
    </svg>
    <div class="person">
      <h1 class="person__name">WADE CALLOWAY</h1>
      <p class="person__role">Designation</p>
    </div>
    <ul class="contact">
      <li class="contact__item contact__item--address">
        <span class="contact__label">a :</span>215 Mesa Ridge Road 4402<br>
        <span class="contact__indent">Pine Hollow, TX 75410</span>
      </li>
      <li class="contact__item"><span class="contact__label">p :</span>214-555-0187</li>
      <li class="contact__item"><span class="contact__label">e :</span>wade@caldorfx.com</li>
      <li class="contact__item"><span class="contact__label">w :</span>www.caldorfx.com</li>
    </ul>
  </section>
</body>
</html>
```